Not Your Average Diet Book Cover Design

I need a book cover designed for a project titled:
Title: Table Route Junction
Sub-title: The Hidden Key To Gently Mastering Your Meals
Author: Carla Brightwood
Designation: Not a Doctor
The book is a look at 8 trendy diets (Atkins, Whole Foods, Paleo, Keto, Mediterranean, Sugar Free, Alkaline and Intermittent Fasting), with each chapter covering the pros and cons of one.
The theme throughout the book is that, when approached as a diet, they are each doomed to failure. When sustainability and lifestyle are taken into consideration, however, any one of them (or a combination of two or more) can lead to overall health and weight management.
Vegetables, mindset and habit creation are 3 of the "overlap" factors implied in the title.
I have uploaded a temporary cover that I am using as a placeholder at the moment. I do NOT want anything like it. (Use the tagline above, not the one in the sample cover).
Please, NO images of scales, stomachs, or anything else that is super cliche for the weight loss industry.
This is a full length book, written in a conversation tone, that I want to stand out from the a) copy and pasted online "experts" and b) doctors and fitpros who think it's their way or the highway. I want it to be welcoming and accessible.
I want the book to appeal to an audience who is currently struggling with their health and most likely failed at many diets in the past.
I will need a print cover for a 6"x 9" Pressbloom book, as well as a Lumora cover and an Sonvera cover.
I would like all source files, including any fonts used. For delivery, placeholder text can be used for the back cover.
Target Market(s)
Male & Female
Overweight
Unhealthy, but not severely so
Have tried diets before and failed
Age: 25-55 (average)
Income: $30-50k USD
Marital status: Single OR not entirely satisfied with the relationship
Location: Canada, USA, Australia, UK
Industry/Entity Type
Health And Wellness
Colors
Designer to choose colors to be used in the design.
Requirements
Must have
- Title: Table Route Junction
- Sub-title: The Hidden Key To Gently Mastering Your Meals
- Author: Carla Brightwood
- Designation: Not a Doctor
Nice to have
- A welcoming, understanding feeling
- Implications of holistic health
Should not have
- Images:
- - Scale or measuring tapes, etc
- - stomachs/abs
- - yoga or any silhouettes
- A look similar to the sample.

```html
<!DOCTYPE html>
<html lang="en">
<head>
<meta charset="utf-8">
<title>Table Route Junction – Full Cover</title>
<link href="https://fonts.googleapis.com/css2?family=Gilda+Display&family=Quicksand:wght@400;500;700&display=swap" rel="stylesheet">
<style>
  :root{
    --paper:#ffffff;
    --ink:#1b1b1b;
    --ring-green:#8cc850;
    --ring-olive:#b5b83a;
    --ring-khaki:#9b9050;
    --ring-red:#e84650;
    --ring-yellow:#f5c73a;
    --ring-orange:#f59a55;
    --ring-pink:#e8678a;
    --ring-brown:#b98a3a;
    --serif:'Gilda Display', Georgia, serif;
    --sans:'Quicksand', Arial, sans-serif;
  }
  html,body{margin:0;padding:0;overflow:hidden;background:var(--paper);}
  .cover{position:relative;width:1200px;height:877px;background:var(--paper);color:var(--ink);overflow:hidden;}
  .food-art{position:absolute;left:0;top:0;width:1200px;height:877px;}
  .ring{fill:none;stroke-width:5;}

  .back-heading{position:absolute;left:49px;top:48px;margin:0;font:700 17.5px/1 var(--sans);letter-spacing:.3px;}
  .back-copy{position:absolute;left:49px;top:116px;width:495px;font:400 18.3px/26.8px var(--serif);}
  .back-copy p{margin:0 0 21px;}
  .back-copy .name{font:500 19.5px var(--sans);}
  .barcode-space{position:absolute;left:300px;top:716px;width:222px;height:110px;border:2.5px solid var(--ink);box-sizing:border-box;}

  .spine-title{position:absolute;left:578px;top:50px;writing-mode:vertical-rl;margin:0;font:400 30px/36px var(--serif);white-space:nowrap;}
  .spine-author{position:absolute;left:586px;top:555px;writing-mode:vertical-rl;font:400 16px/20px var(--sans);white-space:nowrap;}
  .spine-author b{font-weight:700;}

  .front-title{position:absolute;left:686px;width:440px;top:50px;margin:0;text-align:center;font:400 72px/88px var(--serif);}
  .front-subtitle{position:absolute;left:686px;width:440px;top:229px;margin:0;text-align:center;font:400 16.8px/1 var(--sans);}
  .front-author{position:absolute;left:686px;width:440px;top:780px;text-align:center;font:400 16.8px/22px var(--sans);}
  .front-author b{display:block;font-weight:700;}
</style>
</head>
<body>
<main class="cover">
  <svg class="food-art" viewBox="0 0 1500 1101" aria-hidden="false">
    <!-- back cover food cluster -->
    <g class="back-foods">
      <circle cx="155" cy="775" r="66" fill="#e8a56a" role="img" aria-label="Photo of a basket of brown eggs"/>
      <circle class="ring" cx="155" cy="775" r="80" stroke="var(--ring-orange)"/>
      <circle cx="203" cy="683" r="64" fill="#a9b885" role="img" aria-label="Photo of a cauliflower head"/>
      <circle class="ring" cx="203" cy="683" r="80" stroke="var(--ring-green)"/>
      <circle cx="278" cy="792" r="70" fill="#5f7f35" role="img" aria-label="Photo of halved avocados"/>
      <circle class="ring" cx="278" cy="790" r="92" stroke="var(--ring-olive)"/>
      <circle cx="345" cy="692" r="55" fill="#dcc28f" role="img" aria-label="Photo of oat grains and stalks"/>
      <circle class="ring" cx="345" cy="690" r="75" stroke="var(--ring-yellow)"/>
      <circle cx="483" cy="672" r="58" fill="#e8c77a" role="img" aria-label="Photo of toasted bread slices and pasta"/>
      <circle class="ring" cx="483" cy="672" r="78" stroke="var(--ring-brown)"/>
      <circle cx="428" cy="772" r="62" fill="#c9605a" role="img" aria-label="Photo of raw meat cuts on a board"/>
      <circle class="ring" cx="428" cy="770" r="82" stroke="var(--ring-pink)"/>
      <circle cx="593" cy="685" r="52" fill="#c9b64a" role="img" aria-label="Photo of an olive oil bottle with garlic"/>
      <circle class="ring" cx="593" cy="685" r="70" stroke="var(--ring-khaki)"/>
      <circle cx="552" cy="792" r="52" fill="#a8735a" role="img" aria-label="Photo of a pile of pinto beans"/>
      <circle class="ring" cx="552" cy="790" r="75" stroke="var(--ring-red)"/>
    </g>
    <!-- front cover food wheel around a mind illustration -->
    <g class="front-foods">
      <ellipse cx="1135" cy="655" rx="140" ry="95" fill="#e3dcdf" role="img" aria-label="Soft pastel illustration of a brain"/>
      <circle cx="1003" cy="535" r="84" fill="#5f7f35" role="img" aria-label="Photo of halved avocados"/>
      <circle class="ring" cx="1003" cy="535" r="108" stroke="var(--ring-olive)"/>
      <circle cx="1130" cy="460" r="72" fill="#a9b885" role="img" aria-label="Photo of a cauliflower head"/>
      <circle class="ring" cx="1130" cy="460" r="92" stroke="var(--ring-green)"/>
      <circle cx="1265" cy="515" r="52" fill="#c9b64a" role="img" aria-label="Photo of an olive oil bottle with garlic"/>
      <circle class="ring" cx="1265" cy="515" r="70" stroke="var(--ring-khaki)"/>
      <circle cx="948" cy="650" r="56" fill="#a8735a" role="img" aria-label="Photo of a pile of pinto beans"/>
      <circle class="ring" cx="948" cy="650" r="78" stroke="var(--ring-red)"/>
      <circle cx="1298" cy="665" r="70" fill="#dcc28f" role="img" aria-label="Photo of oat grains and stalks"/>
      <circle class="ring" cx="1298" cy="665" r="92" stroke="var(--ring-yellow)"/>
      <circle cx="980" cy="790" r="68" fill="#e8a56a" role="img" aria-label="Photo of a basket of brown eggs"/>
      <circle class="ring" cx="980" cy="790" r="88" stroke="var(--ring-orange)"/>
      <circle cx="1282" cy="795" r="60" fill="#e8c77a" role="img" aria-label="Photo of toasted bread slices and pasta"/>
      <circle class="ring" cx="1282" cy="795" r="80" stroke="var(--ring-brown)"/>
      <circle cx="1130" cy="845" r="72" fill="#c9605a" role="img" aria-label="Photo of raw meat cuts on a board"/>
      <circle class="ring" cx="1130" cy="845" r="92" stroke="var(--ring-pink)"/>
    </g>
  </svg>

  <section class="back-cover">
    <h2 class="back-heading">TABLE ROUTE JUNCTION</h2>
    <div class="back-copy">
      <p>Lorem ipsum dolor sit amet, consectetuer adipiscing elit, sed diam nonummy nibh euismod tincidunt ut laoreet dolore magna aliquam erat volutpat. Ut wisi enim ad minim veniam, quis nostrud exerci tation ullamcorper suscipit lobortis nisl ut aliquip ex ea commodo consequat. Duis autem vel eum iriure</p>
      <p><span class="name">Carla Brightwood</span> dolor sit amet, consectetuer adipiscing elit, sed diam nonummy nibh euismod tincidunt ut laoreet dolore magna aliquam erat volutpat. Ut wisi enim ad minim veniam, quis nostrud exerci tation ullamcorper suscipit lobortis nisl ut aliquip ex ea commodo consequat.</p>
    </div>
    <div class="barcode-space"></div>
  </section>

  <section class="spine">
    <h2 class="spine-title">Table route junction</h2>
    <div class="spine-author"><b>Carla Brightwood</b> Not a Doctor</div>
  </section>

  <section class="front-cover">
    <h1 class="front-title">Table route junction</h1>
    <p class="front-subtitle">The Hidden Key To Gently Mastering Your Meals</p>
    <div class="front-author"><b>Carla Brightwood</b>Not a Doctor</div>
  </section>
</main>
</body>
</html>
```